Upgrade and redesign The Corvane Foundation.org wesite

Completely redo our website. Add technical and support information, news updates, add functionality that allows easy donations and volunteer sign up capability. Integrate with CRM Software.

```html
<!DOCTYPE html>
<html lang="en">
<head>
<meta charset="utf-8">
<title>The Corvane Foundation</title>
<link href="https://fonts.googleapis.com/css2?family=Libre+Caslon+Text:wght@400;700&family=Poppins:wght@400;500;600&display=swap" rel="stylesheet">
<style>
:root{
  --navy:#2f2a6d;
  --navy-deep:#262159;
  --orange:#f4662f;
  --orange-soft:#f8923c;
  --peach:#f6d3b6;
  --ink:#2f2a6d;
  --muted:#6d6b7d;
  --line:#f2b9a2;
  --white:#ffffff;
  --serif:'Libre Caslon Text', Georgia, serif;
  --sans:'Poppins', Arial, sans-serif;
}
*{margin:0;padding:0;box-sizing:border-box}
html,body{width:1200px;height:3899px;overflow:hidden;background:var(--white);font-family:var(--sans);color:var(--muted)}
.page{position:relative;width:1200px;height:3899px}
.abs{position:absolute}
.serif-title{font-family:var(--serif);font-weight:400;color:var(--ink);letter-spacing:1px;text-transform:uppercase}

/* hero */
.hero{left:0;top:0;width:1200px;height:631px;background:var(--navy)}
.hero-glow{left:520px;top:0;width:680px;height:631px;background:radial-gradient(ellipse at 70% 45%,rgba(70,62,140,.55),rgba(47,42,109,0) 70%)}
.brand{left:94px;top:92px;width:120px;color:var(--white);font-family:var(--sans);font-size:15px;font-weight:500;line-height:1.15;letter-spacing:.5px}
.brand-mark{left:118px;top:30px;width:54px;height:54px;border-radius:50%;border:2px solid rgba(255,255,255,.85)}
.nav{left:282px;top:50px;display:flex;align-items:center;gap:34px;font-size:11.5px;font-weight:500;color:var(--white)}
.nav-home{width:14px;height:14px}
.nav-cta{left:981px;top:42px;width:125px;height:36px;border-radius:18px;background:var(--white);color:var(--ink);font-size:11px;font-weight:600;display:flex;align-items:center;justify-content:center}
.hero-title{left:92px;top:230px;font-size:68px;line-height:66px;color:var(--white);letter-spacing:3px;white-space:nowrap}
.hero-text{left:92px;top:380px;width:400px;font-size:12px;line-height:17px;color:#e7e5f4}
.hero-arrow{width:48px;height:48px;border-radius:50%;display:flex;align-items:center;justify-content:center}
.hero-arrow.prev{left:93px;top:530px;border:1.5px solid var(--white)}
.hero-arrow.next{left:152px;top:530px;background:linear-gradient(135deg,var(--orange),var(--orange-soft))}
.hero-photo-main{left:656px;top:164px;width:444px;height:444px;border-radius:50%;background:linear-gradient(160deg,#d9dee6 0%,#a9b8c8 45%,#2d4a6e 100%)}
.hero-photo-small{left:545px;top:464px;width:232px;height:232px;border-radius:50%;border:6px solid #eef0f5;background:linear-gradient(160deg,#d8e2ec,#8d99a8 60%,#3b3a42);box-shadow:0 8px 18px rgba(0,0,0,.25)}
.hero-globe{left:948px;top:124px;width:96px;height:96px;border-radius:50%;background:var(--orange)}
.hero-dot{left:1057px;top:250px;width:44px;height:44px;border-radius:50%;background:var(--orange-soft)}

/* who we are */
.who-art{left:227px;top:779px;width:295px;height:265px;border-radius:48% 52% 40% 60%;background:linear-gradient(135deg,#e3e1ef,#c9c5e2)}
.who-title{left:569px;top:780px;font-size:36px}
.who-text{left:569px;top:833px;width:420px;font-size:11.5px;line-height:17.5px}
.who-text p+p{margin-top:13px}
.btn-orange{background:linear-gradient(90deg,var(--orange),var(--orange-soft));color:var(--white);font-weight:600;border-radius:20px;display:flex;align-items:center;justify-content:center}
.who-btn{left:569px;top:1001px;width:120px;height:40px;font-size:10.5px}

/* what we do */
.accent-disc{left:80px;top:1101px;width:158px;height:158px;border-radius:50%;background:radial-gradient(circle,#fbe7d6 0%,var(--peach) 100%)}
.wwd-photo-main{left:91px;top:1123px;width:438px;height:438px;border-radius:50%;background:linear-gradient(150deg,#eceff1,#b9c0c4 50%,#6a5e52)}
.wwd-photo-small{left:418px;top:1304px;width:222px;height:222px;border-radius:50%;border:5px solid var(--white);background:linear-gradient(150deg,#cfd9df,#7e8f9a 60%,#3f4c56)}
.wwd-title{left:714px;top:1140px;font-size:36px}
.wwd-list{left:714px;top:1206px;width:392px;list-style:none}
.wwd-list li{height:71px;display:flex;align-items:center;gap:20px;border-bottom:1px solid var(--line);font-family:var(--serif);font-size:14px;color:var(--ink);letter-spacing:.6px;text-transform:uppercase;padding-left:4px}
.wwd-list li:last-child{border-bottom:none}
.wwd-list svg{width:40px;height:40px;flex:none}

/* science */
.science{left:0;top:1649px;width:1200px;height:525px;background:var(--navy)}
.science-title{left:0;top:1748px;width:1200px;text-align:center;font-size:36px;color:var(--white)}
.science-card{top:1814px;width:165px;height:223px;border-radius:14px}
.science-label{top:2053px;width:165px;text-align:center;font-family:var(--serif);font-size:14px;line-height:19px;color:var(--white);letter-spacing:.6px;text-transform:uppercase}

/* innovative */
.inno-title{left:0;top:2254px;width:1200px;text-align:center;font-size:38px}
.inno-sub{left:0;top:2305px;width:1200px;text-align:center;font-size:12px}
.inno-core{left:463px;top:2353px;width:272px;height:272px;border-radius:50%;background:var(--navy)}
.inno-core-art{left:516px;top:2406px;width:166px;height:166px;border-radius:50%;background:linear-gradient(135deg,#4a4492,#3a3580)}
.inno-icon{width:86px;height:86px;border-radius:50%;background:linear-gradient(135deg,var(--orange),var(--orange-soft));border:4px solid var(--white);display:flex;align-items:center;justify-content:center}
.inno-icon svg{width:40px;height:40px}
.inno-item{width:330px}
.inno-item h3{font-family:var(--serif);font-weight:400;font-size:14px;color:var(--ink);letter-spacing:.6px;text-transform:uppercase}
.inno-item p{font-size:11.5px;margin-top:4px}
.inno-item.left{text-align:right}
.inno-rule{height:1px;background:#e3e2ea;width:314px;top:2483px}

/* news */
.news-title{left:0;top:2700px;width:1200px;text-align:center;font-size:38px}
.news-card{top:2776px;width:271px;height:406px;border-radius:16px;background:var(--white);box-shadow:0 10px 28px rgba(40,35,90,.12);overflow:hidden}
.news-img{height:207px}
.news-body{padding:28px 28px 0}
.news-body h3{font-family:var(--serif);font-weight:400;font-size:12.5px;line-height:15px;color:var(--ink);text-transform:uppercase;letter-spacing:.3px}
.news-date{margin-top:8px;font-size:10px;font-weight:600;color:var(--orange)}
.news-body p{margin-top:12px;font-size:10px;line-height:15.5px}
.news-arrow{width:50px;height:50px;border-radius:50%;display:flex;align-items:center;justify-content:center;top:2934px}
.news-arrow.prev{left:66px;border:1.5px solid var(--ink);background:var(--white)}
.news-arrow.next{left:1082px;background:linear-gradient(135deg,var(--orange),var(--orange-soft))}

/* involved */
.involved{left:0;top:3294px;width:1200px;height:196px;background:var(--navy)}
.involved-title{left:92px;top:3358px;font-size:56px;color:var(--white);letter-spacing:2px;white-space:nowrap}
.inv-btn{top:3371px;width:148px;height:42px;border-radius:21px;font-size:12px;font-weight:600;color:var(--white);display:flex;align-items:center;justify-content:center;gap:8px}
.inv-btn.donate{left:799px;background:linear-gradient(90deg,var(--orange),var(--orange-soft))}
.inv-btn.volunteer{left:955px;border:1.5px solid var(--white)}
.inv-btn svg{width:20px;height:20px}

/* footer */
.footer-brand{left:92px;top:3700px;font-size:24px;line-height:27px;font-weight:500;color:var(--ink);letter-spacing:.5px}
.footer-mark{left:120px;top:3590px;width:96px;height:96px;border-radius:50%;border:2px solid var(--ink)}
.footer-col{top:3576px}
.footer-col h4{font-family:var(--serif);font-weight:400;font-size:15px;color:var(--ink);letter-spacing:.6px;text-transform:uppercase;margin-bottom:16px}
.footer-col ul{list-style:none}
.footer-col li{font-size:10.5px;line-height:25px}
.contact li{display:flex;gap:10px;line-height:15px;margin-bottom:11px}
.contact svg{width:12px;height:12px;flex:none;margin-top:2px}
.footer-rule{left:92px;top:3835px;width:1016px;height:1px;background:#e0dfe8}
.copyright{left:0;top:3860px;width:1200px;text-align:center;font-family:var(--serif);font-size:10px;color:var(--ink);letter-spacing:.3px}
.chat{left:1128px;top:3820px;width:46px;height:46px;border-radius:50%;background:var(--navy);display:flex;align-items:center;justify-content:center}
</style>
</head>
<body>
<div class="page">

  <!-- Hero -->
  <section class="abs hero"></section>
  <div class="abs hero-glow"></div>
  <div class="abs brand-mark"></div>
  <div class="abs brand">The Corvane<br>Foundation</div>
  <nav class="abs nav">
    <svg class="nav-home" viewBox="0 0 14 14"><path d="M1 7L7 1.5 13 7h-2v6H8.5V9h-3v4H3V7z" fill="#fff"/></svg>
    <span>Who we are</span><span>What we do</span><span>The Science of pain</span><span>News in pain research</span><span>Innovative solutions</span>
  </nav>
  <div class="abs nav-cta">GET INVOLVED!</div>
  <h1 class="abs serif-title hero-title">The Corvane<br>Foundation</h1>
  <p class="abs hero-text">The Corvane Foundation's works to empower and support those with chronic pain by promoting innovative research, equitable access to evidence-based care, and improving communication between healthcare providers and suffering patients.</p>
  <div class="abs hero-arrow prev"><svg width="10" height="10" viewBox="0 0 10 10"><path d="M6.5 1.5L3 5l3.5 3.5" stroke="#fff" stroke-width="1.6" fill="none"/></svg></div>
  <div class="abs hero-arrow next"><svg width="10" height="10" viewBox="0 0 10 10"><path d="M3.5 1.5L7 5 3.5 8.5" stroke="#fff" stroke-width="1.6" fill="none"/></svg></div>
  <div class="abs hero-photo-main" role="img" aria-label="Photo of a nurse pushing a smiling woman in a wheelchair through a clinic corridor"></div>
  <svg class="abs" style="left:640px;top:150px" width="500" height="500" viewBox="0 0 500 500"><circle cx="253" cy="240" r="228" fill="none" stroke="#f08a3c" stroke-width="1.5"/></svg>
  <div class="abs hero-globe" role="img" aria-label="Orange globe illustration"></div>
  <div class="abs hero-dot"></div>
  <div class="abs hero-photo-small" role="img" aria-label="Photo of two men sharing a phone screen outdoors"></div>

  <!-- Who we are -->
  <div class="abs who-art" role="img" aria-label="Ornamental patterned dove illustration in navy"></div>
  <h2 class="abs serif-title who-title">Who we are</h2>
  <div class="abs who-text">
    <p>We strive to advance pain research, improve treatment accessibility, and foster collaboration among scientists, healthcare professionals, and patients to develop groundbreaking solutions.</p>
    <p>Elias Corvane founded the Corvane Foundation with a vision: to bridge the gap between medical research and patient care. After witnessing the challenges faced by those with chronic pain, he committed to driving innovation in pain management.</p>
  </div>
  <div class="abs btn-orange who-btn">READ MORE</div>

  <!-- What we do -->
  <div class="abs accent-disc" role="img" aria-label="Soft peach decorative pattern behind the photo"></div>
  <div class="abs wwd-photo-main" role="img" aria-label="Photo of a masked man greeting a colleague with a fist bump in an office"></div>
  <div class="abs wwd-photo-small" role="img" aria-label="Photo of a doctor speaking with an older patient"></div>
  <h2 class="abs serif-title wwd-title">What we do</h2>
  <ul class="abs wwd-list">
    <li><svg viewBox="0 0 40 40" fill="none" stroke="#2f2a6d" stroke-width="1.6"><path d="M6 12l14-6 14 6-14 6z"/><path d="M12 15v6c4 3 12 3 16 0v-6"/><rect x="8" y="25" width="24" height="4"/><rect x="10" y="29" width="22" height="4"/><rect x="7" y="33" width="26" height="3"/></svg>Education in pain</li>
    <li><svg viewBox="0 0 40 40" fill="none" stroke="#2f2a6d" stroke-width="1.6"><path d="M20 32c-8-6-12-10-12-15a6 6 0 0 1 12-2 6 6 0 0 1 12 2c0 5-4 9-12 15z"/><path d="M10 20h6l2-4 3 8 2-4h7"/></svg>Inovative care</li>
    <li><svg viewBox="0 0 40 40" fill="none" stroke="#2f2a6d" stroke-width="1.6"><rect x="9" y="5" width="18" height="28" rx="2"/><path d="M13 11h10M13 16h10M13 21h6"/><circle cx="27" cy="28" r="6"/><path d="M24.5 28l2 2 3.5-4"/></svg>Governmental policy</li>
    <li><svg viewBox="0 0 40 40" fill="none" stroke="#2f2a6d" stroke-width="1.6"><circle cx="12" cy="12" r="6"/><circle cx="28" cy="12" r="6"/><path d="M18 12h4M12 18v6l8 6 8-6v-6"/><circle cx="20" cy="32" r="3"/></svg>Updates in cutting edge research</li>
    <li><svg viewBox="0 0 40 40" fill="none" stroke="#2f2a6d" stroke-width="1.6"><path d="M8 34h26M12 34V14h6v20M22 34V8h6v26"/><path d="M10 10h10M20 5h10"/></svg>Access to clinical trials</li>
  </ul>

  <!-- Science of pain -->
  <section class="abs science"></section>
  <svg class="abs" style="left:0;top:1649px" width="520" height="230" viewBox="0 0 520 230"><path d="M0 215c90-20 150-70 200-140C240 20 300 0 340 40c40 40 90 40 140-40" stroke="#e8906a" stroke-width="1.3" fill="none" opacity=".8"/></svg>
  <h2 class="abs serif-title science-title">The Science of pain</h2>
  <div class="abs science-card" style="left:62px;background:linear-gradient(170deg,#b9d3e6,#8c8277 70%,#5b4f46)" role="img" aria-label="Photo of a man bending over holding his knees after a run"></div>
  <div class="abs science-card" style="left:244px;background:linear-gradient(170deg,#dfe1df,#6f84a6 60%,#c7c5c2)" role="img" aria-label="Photo of a man on a sofa holding his neck in pain"></div>
  <div class="abs science-card" style="left:425px;background:linear-gradient(170deg,#cfc8b6,#e2cf5a 55%,#a9a08a)" role="img" aria-label="Photo of an older woman holding her shoulder"></div>
  <div class="abs science-card" style="left:607px;background:linear-gradient(170deg,#e6eae7,#9fb3b2 55%,#7c8b8f)" role="img" aria-label="Photo of a therapist treating a patient's back"></div>
  <div class="abs science-card" style="left:789px;background:linear-gradient(170deg,#d9d5cf,#8d9bb1 55%,#e6e1da)" role="img" aria-label="Photo of a doctor writing a prescription for a patient"></div>
  <div class="abs science-card" style="left:970px;background:linear-gradient(170deg,#e9e6e0,#9bb1c6 55%,#6d86a6)" role="img" aria-label="Photo of a caregiver supporting an older woman with a cane"></div>
  <div class="abs science-label" style="left:62px">Acute<br>pain</div>
  <div class="abs science-label" style="left:244px">Chronic<br>pain</div>
  <div class="abs science-label" style="left:425px">Diagnosing<br>pain</div>
  <div class="abs science-label" style="left:607px">Pain<br>therapy</div>
  <div class="abs science-label" style="left:789px">Emerging<br>treatments</div>
  <div class="abs science-label" style="left:970px">Supportive<br>care</div>

  <!-- Innovative solutions -->
  <h2 class="abs serif-title inno-title">Innovative solutions</h2>
  <p class="abs inno-sub">We explore groundbreaking approaches to pain relief, including:</p>
  <div class="abs inno-core"></div>
  <div class="abs inno-core-art" role="img" aria-label="Ornamental white dove illustration"></div>
  <div class="abs inno-icon" style="left:432px;top:2367px"><svg viewBox="0 0 40 40" fill="none" stroke="#fff" stroke-width="1.8"><path d="M6 24h28l-3 10H9z"/><circle cx="14" cy="18" r="5"/><path d="M22 19l6-10 4 3-5 8"/></svg></div>
  <div class="abs inno-icon" style="left:683px;top:2367px"><svg viewBox="0 0 40 40" fill="none" stroke="#fff" stroke-width="1.8"><path d="M13 34v-7c-4-3-6-7-5-12 2-7 10-10 17-7 5 3 7 8 6 13l3 5-4 1v4h-6v3"/><circle cx="20" cy="17" r="4"/></svg></div>
  <div class="abs inno-icon" style="left:432px;top:2525px"><svg viewBox="0 0 40 40" fill="none" stroke="#fff" stroke-width="1.8"><rect x="7" y="7" width="26" height="26" rx="4"/><circle cx="20" cy="18" r="5"/><path d="M12 31c1-5 4-7 8-7s7 2 8 7"/></svg></div>
  <div class="abs inno-icon" style="left:683px;top:2525px"><svg viewBox="0 0 40 40" fill="none" stroke="#fff" stroke-width="1.8"><path d="M8 14c4-6 20-6 24 0"/><path d="M12 14v18M20 12v20M28 14v18M8 24h24"/></svg></div>
  <div class="abs inno-item left" style="left:82px;top:2384px"><h3>Diet and healthy lifestyle</h3><p>Nutrition strategies to manage inflammation and pain.</p></div>
  <div class="abs inno-item" style="left:788px;top:2384px"><h3>Ketamine therapy</h3><p>A revolutionary treatment for chronic pain.</p></div>
  <div class="abs inno-item left" style="left:82px;top:2549px"><h3>Sleep and pain</h3><p>The connection between restorative sleep and pain</p></div>
  <div class="abs inno-item" style="left:788px;top:2549px"><h3>Asian alternative therapies</h3><p>Herbal medicine, and holistic healing techniques.</p></div>
  <div class="abs inno-rule" style="left:98px"></div>
  <div class="abs inno-rule" style="left:788px"></div>

  <!-- News -->
  <h2 class="abs serif-title news-title">News in pain research</h2>
  <div class="abs news-arrow prev"><svg width="10" height="10" viewBox="0 0 10 10"><path d="M6.5 1.5L3 5l3.5 3.5" stroke="#2f2a6d" stroke-width="1.6" fill="none"/></svg></div>
  <div class="abs news-arrow next"><svg width="10" height="10" viewBox="0 0 10 10"><path d="M3.5 1.5L7 5 3.5 8.5" stroke="#fff" stroke-width="1.6" fill="none"/></svg></div>
  <article class="abs news-card" style="left:172px">
    <div class="news-img" style="background:linear-gradient(135deg,#7f6a56,#5f8a4a 50%,#c9b9a6)" role="img" aria-label="Photo of a fresh salad bowl with fitness gear on a table"></div>
    <div class="news-body"><h3>A healthy diet helps the weighty battle with chronic pain</h3><div class="news-date">Dec. 8, 2024</div><p>New research shows that adopting a healthy diet can reduce the severity of chronic pain, presenting an easy and accessible way for sufferers to better manage their...</p></div>
  </article>
  <article class="abs news-card" style="left:464px">
    <div class="news-img" style="background:linear-gradient(135deg,#d8d8d8,#a9a19a 55%,#6f6a66)" role="img" aria-label="Photo of a woman holding her head with a headache"></div>
    <div class="news-body"><h3>Nerve stimulation: the brain is not always listening</h3><div class="news-date">Jan. 27, 2025</div><p>Various diseases can be treated by stimulating the vagus nerve in the ear with electrical signals. However, this technique does not always work. A study has now shown...</p></div>
  </article>
  <article class="abs news-card" style="left:757px">
    <div class="news-img" style="background:linear-gradient(135deg,#7fa6d8,#e8c6b8 55%,#f0d8cc)" role="img" aria-label="Photo of a gloved clinician giving an injection in a patient's back"></div>
    <div class="news-body"><h3>Epidural steroid injections for chronic back pain</h3><div class="news-date">Feb. 12, 2025</div><p>Scientists have developed a new systematic review to summarize for neurologists and other clinicians the evidence for epidural steroid injections and whether they reduce...</p></div>
  </article>

  <!-- Getting involved -->
  <section class="abs involved"></section>
  <h2 class="abs serif-title involved-title">Getting involved!</h2>
  <div class="abs inv-btn donate"><svg viewBox="0 0 20 20" fill="none" stroke="#fff" stroke-width="1.5"><path d="M10 9c-3-2-5-4-5-6a2.5 2.5 0 0 1 5-.5A2.5 2.5 0 0 1 15 3c0 2-2 4-5 6z"/><path d="M2 13l4-2h4l3 1h3l2 2-6 3-6-1-4 1"/></svg>DONATE!</div>
  <div class="abs inv-btn volunteer"><svg viewBox="0 0 20 20" fill="none" stroke="#fff" stroke-width="1.5"><path d="M6 18v-8l-2-3V4h2v3M8 10V2h2v7M10 9V3h2v6M12 9V4h2v7l-2 4v3"/></svg>VOLUNTEER</div>

  <!-- Footer -->
  <div class="abs footer-mark"></div>
  <div class="abs footer-brand">The Corvane<br>Foundation</div>
  <div class="abs footer-col" style="left:331px"><h4>Quick links</h4><ul><li>Who we are</li><li>What we do</li><li>The Science of pain</li><li>News in pain research</li><li>Innovative solutions</li><li>Get Involved</li></ul></div>
  <div class="abs footer-col" style="left:523px"><h4>Science pain</h4><ul><li>Acute Pain</li><li>Chronic Pain</li><li>Diagnosing Pain</li><li>Pain Therapy</li><li>Emerging Treatments</li><li>Supportive Care</li></ul></div>
  <div class="abs footer-col" style="left:707px"><h4>Service area</h4><ul><li>Orange County, CA</li><li>Riverside County, CA</li><li>San Bernardino County, CA</li><li>Ventura County, CA</li><li>Los Angeles County, CA</li><li>San Diego County, CA</li></ul></div>
  <div class="abs footer-col contact" style="left:909px;width:210px"><h4>Contact us</h4><ul>
    <li style="margin-top:8px"><svg viewBox="0 0 12 12"><path d="M6 11S2 7 2 4.5a4 4 0 0 1 8 0C10 7 6 11 6 11z" fill="#f4662f"/><circle cx="6" cy="4.5" r="1.4" fill="#fff"/></svg><span style="font-size:10.5px">1420 Harbor View Lane, Los Angeles, CA, United States, 90210</span></li>
    <li><svg viewBox="0 0 12 12"><path d="M3 1l2 2.5-1 1.5c.8 1.5 1.6 2.3 3 3l1.5-1L11 9l-1.5 2C5 10.5 1.5 7 1 2.5z" fill="#f4662f"/></svg><span style="font-size:10.5px">Mobile:<br>+1 310-555-0148</span></li>
    <li><svg viewBox="0 0 12 12"><rect x="1" y="2.5" width="10" height="7" fill="#f4662f"/><path d="M1 3l5 3.5L11 3" stroke="#fff" fill="none"/></svg><span style="font-size:10.5px">Email:<br>info@corvanefoundation.org</span></li>
    <li><svg viewBox="0 0 12 12"><circle cx="6" cy="6" r="5" fill="#f4662f"/><path d="M6 3v3h2.5" stroke="#fff" fill="none"/></svg><span style="font-size:10.5px">Hours:<br>Closed now</span></li>
  </ul></div>
  <div class="abs footer-rule"></div>
  <p class="abs copyright">© COPYRIGHT 2025, THE CORVANE FOUNDATION, ALL RIGHTS RESERVED</p>
  <div class="abs chat"><svg width="26" height="24" viewBox="0 0 26 24"><path d="M3 4h20v13H11l-6 5v-5H3z" fill="#fff"/><circle cx="9" cy="10.5" r="1.5" fill="#2f2a6d"/><circle cx="13" cy="10.5" r="1.5" fill="#2f2a6d"/><circle cx="17" cy="10.5" r="1.5" fill="#2f2a6d"/></svg></div>

</div>
</body>
</html>
```